International business needs a web page design

We need a web page design for a new service that our new "sub-company" of our existing company will offer. We are based in Denmark, and our new "sub-company" is called 'Velkari'. The service we offer is automated server configuration and In-Depth monitoring, and optional operations support. Our monitoring has a lot of graphs (like those seen here: https://velkari.example/ with either black or white background ) and the website needs to communicate a sense of Security/safety and that our customers can relax, because we have the full overview of their service and servers. The website should not be with black background.

We deliver low price, high quality and professional operations - which we can do, because we automate it and have people with 15+ years of experience doing so.

We have attached :
a file with our logo : velkari
a file showing the content of the frontage : frontpage
a file showing the content of the user page(for logged in users) : User page
a file showing the pop-up dialog "page" : CallToAction_route
a file showing the 3-steps for the frontpage : 3-step for frontpage

Target Market(s)

Chief Technological officers (CTO's) and Developers (small business, run by developers) - who needs professional IT operations.

Industry/Entity Type

Business

Coding

Coded - Design and coding required

Number of Pages Required

3 page

Requirements
Must have
• Frontpage :
• A lot of visualization(some with people too) rather than a lot of text
• A short, describing text on front page telling what people get
• 3 steps showing people how it works. (Could be presented in a video placed on top of a big front image or perhaps with all 3 steps/pictures shown at the same time or perhaps in a completely different way).
Nice to have
• A big front image(perhaps a person with a cellphone showing graphs and a "all okay" message) with a text and the 3-steps pictures/or video on top of it
• 3 boxes under the front image/top of the site showing what benefits people get from the service
Should not have
• Not a black/dark site

```html
<!DOCTYPE html>
<html lang="en">
<head>
<meta charset="utf-8">
<title>Velkari – Instant server setup & in-depth monitoring</title>
<link href="https://fonts.googleapis.com/css2?family=Mulish:wght@400;600;700&display=swap" rel="stylesheet">
<style>
  :root {
    --blue: #1ba3dc;
    --blue-dark: #1286ba;
    --ink: #1d1d1d;
    --text: #333;
    --muted: #777;
    --grey-btn: #c9c9c9;
    --hero-band: #ececec;
    --section-bg: #f4f4f4;
    --card-bg: #fafafa;
    --white: #ffffff;
  }
  * { box-sizing: border-box; margin: 0; padding: 0; }
  html, body { width: 1089px; height: 1200px; overflow: hidden; background: var(--white); }
  body { position: relative; font-family: "Mulish", Arial, sans-serif; color: var(--text); }

  /* header */
  .site-header { position: absolute; left: 0; top: 0; width: 1089px; height: 99px; background: var(--white); }
  .brand { position: absolute; left: 147px; top: 20px; display: flex; align-items: center; gap: 10px; text-decoration: none; }
  .brand-dot { width: 58px; height: 58px; border-radius: 50%; background: var(--blue); }
  .brand-name { font-size: 34px; font-weight: 600; color: var(--ink); letter-spacing: -0.5px; }
  .main-nav a { position: absolute; top: 44px; font-size: 12px; font-weight: 600; color: var(--ink); text-decoration: none; letter-spacing: 0.3px; }
  .main-nav a.active { color: var(--blue); }
  .nav-underline { position: absolute; left: 510px; top: 96px; width: 37px; height: 3px; background: var(--blue); }

  /* hero */
  .hero { position: absolute; left: 0; top: 99px; width: 1089px; height: 449px; background: linear-gradient(180deg, #dcdcdc 0%, #e7e7e7 60%, #ededed 100%); overflow: hidden; }
  .hero-band { position: absolute; left: 0; top: 379px; width: 1089px; height: 70px; background: var(--hero-band); }
  .device-monitor { position: absolute; left: 147px; top: 64px; width: 419px; height: 355px; border-radius: 8px 8px 4px 4px; background: linear-gradient(180deg, #1f1f1f 0%, #2b2b2b 70%, #b9b9b9 71%, #d4d4d4 100%); }
  .device-phone { position: absolute; left: 538px; top: 165px; width: 126px; height: 253px; border-radius: 18px; background: linear-gradient(180deg, #f4f1ec 0%, #ffffff 40%, #e9e6e0 100%); box-shadow: 0 0 0 1px #d8d2c6; }
  .hero-title { position: absolute; left: 602px; top: 102px; font-size: 37px; font-weight: 400; color: var(--ink); letter-spacing: 0.5px; white-space: nowrap; }
  .benefit-list { position: absolute; left: 688px; top: 166px; list-style: none; }
  .benefit-list li { display: flex; align-items: center; gap: 12px; height: 31px; font-size: 15.5px; color: var(--ink); white-space: nowrap; }
  .benefit-list svg { width: 18px; height: 18px; }
  .btn { display: inline-flex; align-items: center; justify-content: center; text-decoration: none; color: var(--white); font-weight: 700; border-radius: 2px; white-space: nowrap; }
  .btn-primary { background: linear-gradient(180deg, #2bb3ea 0%, var(--blue) 100%); box-shadow: inset 0 -3px 0 var(--blue-dark); }
  .btn-try { position: absolute; left: 689px; top: 274px; width: 197px; height: 36px; font-size: 16px; }
  .slider-dots { position: absolute; left: 689px; top: 343px; display: flex; gap: 4px; }
  .slider-dots span { width: 14px; height: 14px; border-radius: 50%; background: var(--white); box-shadow: 0 0 2px rgba(0,0,0,.2); }
  .slider-dots span.current { border: 2px solid var(--blue); background: transparent; }

  /* expertise */
  .expertise-title { position: absolute; left: 147px; top: 589px; font-size: 23.5px; line-height: 29px; font-weight: 400; color: var(--ink); width: 450px; white-space: nowrap; }
  .expertise-title strong { color: var(--blue); font-weight: 700; }
  .expertise-text { position: absolute; left: 147px; top: 684px; width: 430px; font-size: 12px; line-height: 14px; color: var(--ink); }
  .btn-setup { position: absolute; left: 147px; top: 748px; width: 229px; height: 43px; font-size: 16px; letter-spacing: 0.3px; }

  .testimonials { position: absolute; left: 599px; top: 591px; width: 345px; height: 200px; background: var(--card-bg); box-shadow: 0 8px 10px -8px rgba(0,0,0,.15); text-align: center; }
  .quote-mark { position: absolute; left: 156px; top: -8px; width: 32px; height: 30px; }
  .testimonials h3 { position: absolute; left: 0; top: 27px; width: 100%; font-size: 15.5px; font-weight: 400; color: var(--blue); letter-spacing: 0.3px; }
  .testimonials blockquote { position: absolute; left: 28px; top: 54px; width: 289px; font-size: 12px; line-height: 14.5px; color: #444; }
  .t-arrow { position: absolute; top: 86px; width: 8px; height: 16px; }
  .author { position: absolute; left: 112px; top: 132px; display: flex; align-items: center; gap: 6px; text-align: left; }
  .avatar { width: 26px; height: 26px; border-radius: 50%; background: linear-gradient(135deg, #c99b7a, #8a5a3e); }
  .author-name { font-size: 11px; color: var(--ink); font-weight: 600; line-height: 13px; }
  .author-role { font-size: 9.5px; color: #999; }
  .see-all { position: absolute; left: 0; bottom: 0; width: 100%; height: 21px; line-height: 21px; background: #ececec; font-size: 11px; font-weight: 700; color: #bbb; letter-spacing: 0.5px; }

  /* features */
  .features { position: absolute; left: 0; top: 836px; width: 1089px; height: 274px; background: var(--section-bg); }
  .feature-card { position: absolute; top: 12px; width: 261px; height: 252px; background: var(--card-bg); }
  .feature-icon { position: absolute; left: 19px; top: 26px; width: 42px; height: 36px; }
  .feature-card h3 { position: absolute; left: 69px; top: 30px; width: 190px; font-size: 15.5px; line-height: 19px; font-weight: 400; color: var(--ink); white-space: nowrap; letter-spacing: -0.1px; }
  .feature-card p { position: absolute; left: 20px; top: 88px; width: 225px; font-size: 11px; line-height: 15.5px; color: var(--muted); }
  .btn-read { position: absolute; left: 20px; top: 185px; width: 91px; height: 31px; font-size: 12px; }
  .btn-muted { background: var(--grey-btn); box-shadow: inset 0 -3px 0 #b3b3b3; }

  /* footer */
  .site-footer { position: absolute; left: 0; top: 1110px; width: 1089px; height: 90px; background: var(--white); }
  .footer-nav { position: absolute; left: 147px; top: 36px; display: flex; gap: 16px; font-size: 12px; white-space: nowrap; }
  .footer-nav a { color: #444; text-decoration: none; }
  .footer-nav a.active { color: var(--blue); font-weight: 700; }
  .footer-copy { color: #444; }
  .social { position: absolute; left: 864px; top: 32px; display: flex; gap: 7px; }
  .social span { width: 22px; height: 22px; background: #bdbdbd; }
  .social span.hot { background: #e0261b; }
</style>
</head>
<body>

<header class="site-header">
  <a class="brand" href="https://velkari.example/">
    <span class="brand-dot"></span>
    <span class="brand-name">Velkari</span>
  </a>
  <nav class="main-nav">
    <a class="active" href="#" style="left:512px">HOME</a>
    <a href="#" style="left:596px">SERVICES</a>
    <a href="#" style="left:695px">ABOUT US</a>
    <a href="#" style="left:800px">CONTACT</a>
    <a href="#" style="left:901px">LOGIN</a>
  </nav>
  <span class="nav-underline"></span>
</header>

<section class="hero">
  <div class="hero-band"></div>
  <div class="device-monitor" role="img" aria-label="Desktop monitor showing a dark monitoring dashboard with server graphs"></div>
  <div class="device-phone" role="img" aria-label="Smartphone showing the Velkari network status page with all services OK"></div>
  <h1 class="hero-title">WHAT PEOPLE GET?</h1>
  <ul class="benefit-list">
    <li><svg viewBox="0 0 18 18"><circle cx="9" cy="9" r="8" fill="none" stroke="#444" stroke-width="1.3"/><rect x="5.5" y="5" width="7" height="8" rx="1" fill="none" stroke="#444" stroke-width="1.2"/><path d="M7 8h4M7 10h4" stroke="#444"/></svg>Automated Server Configuration</li>
    <li><svg viewBox="0 0 18 18"><circle cx="9" cy="9" r="8" fill="none" stroke="#444" stroke-width="1.3"/><path d="M6 12V9M8 12V6M10 12V8M12 12V7" stroke="#444" stroke-width="1.3"/></svg>In-depth Monitoring</li>
    <li><svg viewBox="0 0 18 18"><circle cx="9" cy="9" r="8" fill="none" stroke="#444" stroke-width="1.3"/><path d="M6 7a3 3 0 0 1 6 0v3a3 3 0 0 1-3 3" fill="none" stroke="#444" stroke-width="1.3"/></svg>Operations Support</li>
  </ul>
  <a class="btn btn-primary btn-try" href="#">Try It - Free</a>
  <div class="slider-dots"><span></span><span class="current"></span><span></span><span></span></div>
</section>

<h2 class="expertise-title">THE SERVER SETUP IS DONE&nbsp; BY OUR<br>EXPERT SYSADMINS WITH <strong>15+ YEARS</strong><br>OF EXPERIENCE WITH LINUX.</h2>
<p class="expertise-text">Lorem ipsum dolor sit amet, consectetuer adipiscing elit, sed diam nonummy nibh euismod tincidunt ut laoreet dolore magna aliquam erat volutpat.</p>
<a class="btn btn-primary btn-setup" href="#">INSTANT SERVER SETUP</a>

<aside class="testimonials">
  <svg class="quote-mark" viewBox="0 0 32 30"><path d="M2 0h12v14l-5 14H3l4-12H2z M18 0h12v14l-5 14h-6l4-12h-5z" fill="var(--blue)"/></svg>
  <h3>CUSTOMER TESTIMONIALS</h3>
  <svg class="t-arrow" style="left:9px" viewBox="0 0 8 16"><path d="M7 1L1 8l6 7" fill="none" stroke="#ddd"/></svg>
  <svg class="t-arrow" style="right:9px" viewBox="0 0 8 16"><path d="M1 1l6 7-6 7" fill="none" stroke="#ddd"/></svg>
  <blockquote>Lorem ipsum dolor sit amet, consectetur adipisicing elit. Quam totam nulla est, illo molestiae maxime officiis, quae ad, ipsum vitae deserunt molestias eius alias.</blockquote>
  <div class="author">
    <span class="avatar" role="img" aria-label="Customer portrait photo"></span>
    <div><div class="author-name">MyName</div><div class="author-role">CEO, CompanyName</div></div>
  </div>
  <div class="see-all">SEE ALL</div>
</aside>

<section class="features">
  <article class="feature-card" style="left:147px">
    <svg class="feature-icon" viewBox="0 0 56 48"><path d="M0 16h24M0 24h20M0 32h24" stroke="#444" stroke-width="2.5"/><path d="M46 4L31 27h11l-7 17 18-24H41z" fill="none" stroke="#444" stroke-width="2.5" stroke-linejoin="round"/></svg>
    <h3>IT'S FAST AND<br>EASY</h3>
    <p>We have done all the hard work, so you can focus on what you need out of your server - your server will be ready in a few minutes.. ( instant server setup )</p>
    <a class="btn btn-primary btn-read" href="#">READ MORE</a>
  </article>
  <article class="feature-card" style="left:415px">
    <svg class="feature-icon" viewBox="0 0 48 44"><rect x="8" y="2" width="32" height="28" rx="3" fill="none" stroke="#444" stroke-width="2.5"/><rect x="2" y="16" width="44" height="20" rx="3" fill="none" stroke="#444" stroke-width="2.5"/><path d="M7 36v6M41 36v6" stroke="#444" stroke-width="2.5"/></svg>
    <h3>RELAX AND REST<br>ASSURED</h3>
    <p>We will monitor your server and are ready 24/7 to handle issues on your server - so you do not have to be the system expert, we will advise and help you to ensure that you can growwith your success, and handle any emergency</p>
    <a class="btn btn-muted btn-read" href="#">READ MORE</a>
  </article>
  <article class="feature-card" style="left:682px">
    <svg class="feature-icon" viewBox="0 0 48 44"><path d="M2 22l11-11 8 7 16-15" fill="none" stroke="#444" stroke-width="2.5"/><path d="M2 30h11M17 30h11M32 30h11M2 38h11M17 38h11M32 38h11" stroke="#444" stroke-width="3.5"/></svg>
    <h3>ENJOY YOUR DETAILED<br>PERFORMANCE GRAPHS</h3>
    <p>We will tell you, minute-by-minute - how your website performs and how close your server is to it's limits, so you can react in time.</p>
    <a class="btn btn-muted btn-read" href="#">READ MORE</a>
  </article>
</section>

<footer class="site-footer">
  <nav class="footer-nav">
    <a class="active" href="#">Home</a>
    <a href="#">Services</a>
    <a href="#">About Us</a>
    <a href="#">Contact</a>
    <a href="#">Sitemap</a>
    <span class="footer-copy">© 2015 All Rights Reserved.</span>
  </nav>
  <div class="social"><span></span><span class="hot"></span><span></span></div>
</footer>

</body>
</html>
```